Harborline Restoration Business Card Design Phase 2

Professional and clean design. The design colors should flow with the logo. Two-sided card with the website on the back which is:

www.HarborlineRestoration.example.

"Specializing in Water Damage Restoration"

On the front I need the name, email, phone, and logo.

Name: Darnell Vickery
Email: Darnell@HarborlineRestoration.example
Phone: 555-018-2734 for now

I only have the Preview and Thumbnail right now but should have the source files uploaded within a day or two.

Target Market(s)

Flood victims, home owners with water damage from busted pipes etc...

Industry/Entity Type

Business

Contact Information for Business Card

Name: Darnell Vickery

Font styles to use
Serif
Sans Serif

Requirements
Must have
• Business Card Details Info

```html
<!DOCTYPE html>
<html lang="en">
<head>
<meta charset="utf-8">
<title>Harborline Restoration Business Card</title>
<link rel="stylesheet" href="https://fonts.googleapis.com/css2?family=Tinos:wght@400;700&display=swap">
<style>
  :root{
    --bg:#e8e8ea;
    --paper:#ffffff;
    --navy:#1f3a68;
    --text-green:#3a8a2e;
    --deep-green:#1e5e2a;
    --leaf:#6bbf3a;
    --lime:#9ed24a;
    --slate:#2f3f5c;
    --steel:#6f86a8;
    --sky:#4a86b8;
    --sea:#2e6a96;
  }
  *{box-sizing:border-box;margin:0;padding:0}
  html,body{width:1200px;height:800px;overflow:hidden;background:var(--bg)}
  .canvas{position:relative;width:1200px;height:800px;overflow:hidden;background:var(--bg);font-family:"Tinos","Times New Roman",serif}
  .card{position:absolute;width:540px;height:310px;background:var(--paper);overflow:hidden;box-shadow:0 6px 18px rgba(0,0,0,.18)}
  .card-back{left:50px;top:90px}
  .card-front{left:610px;top:400px}
  .card .bands{position:absolute;inset:0;width:100%;height:100%}

  .wordmark{position:absolute;font-family:"Tinos","Times New Roman",serif;font-weight:700;color:var(--navy);line-height:1;letter-spacing:1px}
  .wordmark span{display:block}
  .card-back .wordmark{left:150px;top:40px;font-size:40px}
  .card-front .wordmark{right:24px;top:28px;font-size:32px}

  .back-url{position:absolute;left:70px;top:212px;font-size:20px;line-height:1;font-weight:700;letter-spacing:1.5px;color:var(--deep-green);transform:rotate(-7.4deg);transform-origin:left center;white-space:nowrap}

  .contact{position:absolute;left:28px;top:58px;color:var(--text-green)}
  .contact .name{font-size:22px;font-weight:700;line-height:1}
  .contact .role{font-size:14px;font-weight:700;line-height:1;margin:4px 0 10px 10px}
  .contact ul{list-style:none}
  .contact li{display:flex;align-items:flex-start;gap:8px;font-size:13px;font-weight:700;line-height:1.2;margin-bottom:5px}
  .contact svg{flex:0 0 15px;width:15px;height:15px;fill:none;stroke:var(--text-green);stroke-width:1.8}
  .contact svg.solid{fill:var(--text-green);stroke:none}

  .tagline{position:absolute;left:80px;top:273px;font-size:20px;line-height:1;font-weight:700;color:var(--slate);transform:rotate(-12.5deg);transform-origin:left center;white-space:nowrap}
</style>
</head>
<body>
<main class="canvas">

  <section class="card card-back" aria-label="Business card back">
    <svg class="bands" viewBox="0 0 540 310" aria-hidden="true">
      <defs>
        <linearGradient id="greenFill" x1="0" y1="0" x2="1" y2="1">
          <stop offset="0" stop-color="#7cc43e"/>
          <stop offset="0.6" stop-color="#9ed24a"/>
          <stop offset="1" stop-color="#5aa832"/>
        </linearGradient>
      </defs>
      <polygon points="0,200 540,130 540,144 0,214" fill="#1e5e2a"/>
      <polygon points="0,248 540,178 540,188 0,258" fill="#6bbf3a"/>
      <polygon points="0,264 540,194 540,206 0,276" fill="#2f7a2e"/>
      <polygon points="0,282 540,212 540,310 0,310" fill="url(#greenFill)"/>
      <polygon points="0,300 540,250 540,310 0,310" fill="#4f9a30" opacity=".5"/>
    </svg>
    <div class="wordmark" role="img" aria-label="Harborline Restoration"><span>HARBORLINE</span><span>RESTORATION</span></div>
    <p class="back-url">www.HarborlineRestoration.example</p>
  </section>

  <section class="card card-front" aria-label="Business card front">
    <svg class="bands" viewBox="0 0 540 310" aria-hidden="true">
      <defs>
        <linearGradient id="blueFill" x1="0" y1="0" x2="1" y2="1">
          <stop offset="0" stop-color="#2e6a96"/>
          <stop offset="0.6" stop-color="#4a86b8"/>
          <stop offset="1" stop-color="#2e5f88"/>
        </linearGradient>
      </defs>
      <polygon points="0,270 540,150 540,164 0,284" fill="#2f3f5c"/>
      <polygon points="0,318 540,198 540,208 0,328" fill="#6f86a8"/>
      <polygon points="0,334 540,214 540,224 0,344" fill="#3b5478"/>
      <polygon points="0,350 540,230 540,310 0,310" fill="url(#blueFill)"/>
    </svg>
    <div class="wordmark" role="img" aria-label="Harborline Restoration"><span>HARBORLINE</span><span>RESTORATION</span></div>
    <div class="contact">
      <p class="name">Darnell Vickery</p>
      <p class="role">Owner</p>
      <ul>
        <li><svg class="solid" viewBox="0 0 16 16" aria-hidden="true"><path d="M3 1.5l3 .5 1 3.2-1.8 1.2a8 8 0 0 0 4.4 4.4l1.2-1.8 3.2 1 .5 3c-6.5.8-12.3-5-11.5-11.5z"/></svg>555 018 2734</li>
        <li><svg viewBox="0 0 16 16" aria-hidden="true"><rect x="1.5" y="3.5" width="13" height="9"/><path d="M1.5 3.5l6.5 5 6.5-5M1.5 12.5l5-4.5M14.5 12.5l-5-4.5"/></svg>Darnell@HarborlineRestoration.example</li>
        <li><svg viewBox="0 0 16 16" aria-hidden="true"><rect x="1.5" y="2.5" width="13" height="11"/><path d="M1.5 5.5h13"/></svg>www.HarborlineRestoration.example</li>
        <li><svg class="solid" viewBox="0 0 16 16" aria-hidden="true"><path d="M8 1a5 5 0 0 0-5 5c0 3.6 5 9 5 9s5-5.4 5-9a5 5 0 0 0-5-5zm0 7a2 2 0 1 1 0-4 2 2 0 0 1 0 4z"/></svg>48 Pier Lane<br>02217 Harbor Bay</li>
      </ul>
    </div>
    <p class="tagline">Specializing in Water Damage Restoration</p>
  </section>

</main>
</body>
</html>
```